MEKO Business Card Design

I have a rough idea of the design / layout of the company business card but need help in finalizing the design and quality.

I'm looking for the card to be stand out, but simple, on the front with clear detail on the back with space for some one to write any other detail they need onto the card. The rough draft includes the crinkled graph paper back ground which I quite like for the front.

I will need the card design completed and ready to print in Australian business card standard sizes. This includes detail on all colors, fonts and type faces used as well as copy of the original for editing (inserting other employee details).

I have included the company logo and a rough draft of the card, including the graphic I would like to use for the back ground on the front, I am not sure that the graphic is any good for printing, not the highest res.

Thanks,

Lyle

```html
<!DOCTYPE html>
<html lang="en">
<head>
<meta charset="utf-8">
<title>MEKO Business Card</title>
<link rel="stylesheet" href="https://fonts.googleapis.com/css2?family=Abel&display=swap">
<style>
  :root {
    --page-bg: #eceded;
    --front-dark: #1c1c1c;
    --front-mid: #5a5a5a;
    --front-glow: #8a8a8a;
    --front-ink: #d9d9d9;
    --back-light: #f7f7f7;
    --back-mid: #c9c9c9;
    --back-ink: #1a1a1a;
    --back-soft: #3a3a3a;
    --card-shadow: rgba(0,0,0,0.35);
  }
  * { margin: 0; padding: 0; box-sizing: border-box; }
  html, body {
    width: 1200px; height: 620px; overflow: hidden;
    background: var(--page-bg);
    font-family: "Abel", "Arial Narrow", sans-serif;
  }
  .canvas { position: relative; width: 1200px; height: 620px; }
  .card {
    position: absolute; top: 151px;
    width: 520px; height: 318px; overflow: hidden;
    box-shadow: 3px 4px 8px var(--card-shadow);
  }
  .card-front {
    left: 50px;
    background: radial-gradient(ellipse 70% 60% at 50% 45%, var(--front-glow), var(--front-mid) 55%, var(--front-dark));
  }
  .card-back {
    left: 630px;
    background: linear-gradient(160deg, var(--back-light) 0%, #e3e3e3 45%, var(--back-mid) 100%);
  }
  .card-curves { position: absolute; inset: 0; width: 100%; height: 100%; }
  .front-brand {
    position: absolute; left: 0; right: 0; top: 62px; text-align: center;
    color: var(--front-ink);
  }
  .front-brand .brand-name { font-size: 150px; line-height: 1; letter-spacing: 6px; }
  .front-brand .brand-tagline { font-size: 17px; letter-spacing: 1px; margin-top: 2px; }
  .back-brand { position: absolute; left: 28px; top: 26px; color: var(--back-ink); }
  .back-brand .brand-name { font-size: 64px; line-height: 1; letter-spacing: 3px; }
  .back-brand .brand-tagline { font-size: 10.5px; letter-spacing: 0.5px; color: var(--back-soft); }
  .contact {
    position: absolute; right: 34px; top: 104px; text-align: right; color: var(--back-soft);
  }
  .contact .person-name { font-size: 22px; color: var(--back-ink); line-height: 1.1; }
  .contact .person-role { font-size: 12px; margin-bottom: 8px; }
  .contact .detail { font-size: 13px; line-height: 22px; }
  .address {
    position: absolute; left: 56px; top: 248px; font-size: 18px; color: var(--back-soft);
  }
</style>
</head>
<body>
<main class="canvas">
  <section class="card card-front" aria-label="Card front">
    <svg class="card-curves" viewBox="0 0 520 318" aria-hidden="true">
      <path d="M-20 230 Q260 150 540 230 L540 318 L-20 318 Z" fill="rgba(0,0,0,0.28)"/>
      <path d="M140 -10 Q340 120 300 330" fill="none" stroke="rgba(255,255,255,0.07)" stroke-width="2"/>
    </svg>
    <div class="front-brand">
      <div class="brand-name">MEKO</div>
      <div class="brand-tagline">MEKO SOUND VISION .COM.AU</div>
    </div>
  </section>

  <section class="card card-back" aria-label="Card back">
    <svg class="card-curves" viewBox="0 0 520 318" aria-hidden="true">
      <path d="M-20 200 Q200 120 540 170 L540 318 L-20 318 Z" fill="rgba(255,255,255,0.35)"/>
      <path d="M300 -10 Q420 140 540 200" fill="none" stroke="rgba(255,255,255,0.6)" stroke-width="2"/>
    </svg>
    <div class="back-brand">
      <div class="brand-name">MEKO</div>
      <div class="brand-tagline">MEKO SOUND VISION .COM.AU</div>
    </div>
    <div class="contact">
      <div class="person-name">Ari Bell</div>
      <div class="person-role">CEO</div>
      <div class="detail">T: 0412 808 3316</div>
      <div class="detail">F: 029 471 2260</div>
      <div class="detail">E: hello@mekosv.com.au</div>
      <div class="detail">www.mekosv.com.au</div>
    </div>
    <div class="address">88 Harbour Lane, Kellyvale, Sydney 2000 NSW</div>
  </section>
</main>
</body>
</html>
```